Postcard Design

We need a postcard design for our 10 year anniversary open house. The company is Fernhollow Medical Spa. The web site is www.fernhollowmedicalspa-example.com. We want royal blue, sliver and white colors for the postcard along with a 10 Year image.

Industry/Entity Type

It Company

```html
<!DOCTYPE html>
<html lang="en">
<head>
<meta charset="utf-8">
<title>Fernhollow Medical Spa – 10 Year Anniversary Open House</title>
<link rel="stylesheet" href="https://fonts.googleapis.com/css2?family=Anton&family=Noto+Sans:wght@400&display=swap">
<style>
  :root {
    --royal-blue: #0b47a1;
    --royal-blue-soft: #2a5fb3;
    --silver: #c8ccc8;
    --white: #ffffff;
    --page: #ffffff;
  }
  html, body {
    margin: 0;
    padding: 0;
    width: 1200px;
    height: 811px;
    overflow: hidden;
    background: var(--page);
  }
  .canvas {
    position: relative;
    width: 1200px;
    height: 811px;
    font-family: "Noto Sans", sans-serif;
  }
  .postcard {
    position: absolute;
    left: 248px;
    top: 135px;
    width: 700px;
    height: 538px;
    background: var(--silver);
    overflow: hidden;
  }
  .band {
    position: absolute;
    left: 0;
    width: 100%;
    background: var(--royal-blue);
  }
  .band--top { top: 0; height: 39px; }
  .band--bottom {
    bottom: 0;
    height: 40px;
    display: flex;
    align-items: center;
    justify-content: center;
    color: var(--white);
    font-size: 12.5px;
    letter-spacing: 0.1px;
  }
  .brand-dot {
    position: absolute;
    left: 322px;
    top: 80px;
    width: 56px;
    height: 56px;
    border-radius: 50%;
    background: var(--royal-blue);
  }
  .brand-name {
    position: absolute;
    left: 0;
    width: 100%;
    top: 153px;
    margin: 0;
    text-align: center;
    color: var(--royal-blue);
    font-weight: 400;
    font-size: 54px;
    line-height: 1;
  }
  .tagline {
    position: absolute;
    left: 210px;
    width: 280px;
    top: 248px;
    text-align: center;
    color: var(--royal-blue);
  }
  .tagline__title {
    font-size: 25px;
    line-height: 30px;
    padding-bottom: 2px;
    border-bottom: 2px solid var(--royal-blue);
  }
  .tagline__services {
    font-size: 20.5px;
    line-height: 28px;
  }
  .banner-art {
    position: absolute;
    left: 134px;
    top: 368px;
    width: 433px;
    height: 86px;
    background: linear-gradient(100deg, var(--royal-blue), var(--royal-blue-soft));
  }
  .announcement {
    position: absolute;
    left: 0;
    top: 0;
    width: 700px;
    height: 538px;
  }
  .announcement__headline {
    font-family: "Anton", sans-serif;
    fill: var(--white);
    stroke: var(--royal-blue);
    stroke-width: 3px;
    paint-order: stroke;
    letter-spacing: 0.5px;
  }
  .announcement__banner-text {
    font-family: "Anton", sans-serif;
    fill: var(--white);
    font-size: 27px;
    letter-spacing: 0.5px;
  }
</style>
</head>
<body>
<div class="canvas">
  <section class="postcard" aria-label="Anniversary open house postcard">
    <div class="band band--top"></div>

    <div class="brand-dot" aria-hidden="true"></div>
    <h1 class="brand-name">Fernhollow</h1>

    <div class="tagline">
      <div class="tagline__title">Medical Spa</div>
      <div class="tagline__services">Cosmetic &amp; Laser Services</div>
    </div>

    <div class="banner-art" role="img" aria-label="Waving royal blue ribbon banner with folded ends"></div>

    <svg class="announcement" viewBox="248 135 700 538" aria-label="Join us for our 10 year anniversary open house">
      <defs>
        <path id="banner-curve" d="M470,577 C560,565 650,540 726,515"/>
      </defs>
      <text class="announcement__headline" x="442" y="507" font-size="30">JOIN US FOR OUR</text>
      <text class="announcement__banner-text"><textPath href="#banner-curve">10 YEAR ANNIVERSARY</textPath></text>
      <text class="announcement__headline" x="617" y="592" font-size="30">OPEN HOUSE</text>
    </svg>

    <footer class="band band--bottom">www.fernhollowmedicalspa-example.com; info@fernhollowmedicalspa-example.com</footer>
  </section>
</div>
</body>
</html>
```